Bramford Holloway Inc. needs an innovative idea for letterhead and visiting cards.

Bramford Holloway Inc. is a Canadian brand since 2007. It is a renown dealer of kids and office furniture locally. Moreover, exporting electric fixtures e.g. switches, LED's, down-lights etc. to Middle East and Africa. We have initiated a number of steps including re-branding, to boost our export in 2020. We have successfully designed our new logo a few months ago through 'Mockplanet' and now we are looking for an innovative idea for a letterhead.
Some key points:
• Red, black and white are the three colors used in all our packaging and furniture. (grey is optional)
• Shouldn’t be too wide.
• Use of watermark is preferable.
• You can visit our North American site at www.bramfordhollowayinc.com. Export website of the company will be launched soon. www.bramfordhollowayinc.ca
• Same letterhead will be used locally and internationally.
• Our new logo and sample packaging is attached.

```html
<!DOCTYPE html>
<html lang="en">
<head>
<meta charset="utf-8">
<title>Bramford Holloway Inc. — Business Card</title>
<link href="https://fonts.googleapis.com/css2?family=Montserrat:wght@400;700&family=Roboto:wght@400&display=swap" rel="stylesheet">
<style>
  :root{
    --bg:#d9d9d6;
    --card-white:#ffffff;
    --brand-red:#a50e12;
    --brand-red-dark:#8c0a0d;
    --brand-red-light:#b3161a;
    --ink-grey:#58585a;
    --rule-grey:#6d6d70;
    --on-red:#ffffff;
  }
  *{box-sizing:border-box;margin:0;padding:0}
  html,body{width:1200px;height:801px;overflow:hidden;background:var(--bg)}
  .stage{position:relative;width:1200px;height:801px;background:radial-gradient(ellipse at 40% 30%,#eceae7 0%,var(--bg) 70%)}

  .card{position:absolute;width:540px;height:309px;box-shadow:0 6px 18px rgba(0,0,0,.18);overflow:hidden}

  /* Front */
  .card-front{left:45px;top:246px;background:var(--card-white)}
  .brand{position:absolute;left:34px;top:104px;display:flex;align-items:center;gap:12px}
  .brand-square{width:46px;height:46px;border:3px solid var(--brand-red);border-radius:7px}
  .brand-name{font-family:"Montserrat",sans-serif;font-weight:400;font-size:19px;line-height:1.15;color:var(--ink-grey);letter-spacing:1px;text-transform:uppercase}
  .divider{position:absolute;left:246px;top:62px;width:2px;height:120px;background:var(--rule-grey)}
  .person{position:absolute;left:268px;top:62px}
  .person-name{font-family:"Montserrat",sans-serif;font-weight:700;font-size:19px;color:var(--brand-red);letter-spacing:.5px}
  .person-title{font-family:"Montserrat",sans-serif;font-weight:700;font-size:15px;color:var(--ink-grey);margin-top:2px}
  .contacts{list-style:none;margin-top:18px;font-family:"Roboto",sans-serif;font-size:13px;color:var(--ink-grey)}
  .contacts li{display:flex;align-items:center;gap:7px;height:19px}
  .contacts svg{width:11px;height:11px;flex:none}
  .address-band{position:absolute;left:0;right:0;top:232px;height:32px;background:var(--brand-red);display:flex;align-items:center;padding-left:30px;gap:8px;font-family:"Roboto",sans-serif;font-size:14px;color:var(--on-red)}
  .address-band svg{width:10px;height:13px}
  .base-line{position:absolute;left:0;right:0;top:272px;height:6px;background:var(--brand-red)}

  /* Back */
  .card-back{left:615px;top:246px;background:linear-gradient(160deg,var(--brand-red-light),var(--brand-red-dark))}
  .world-map{position:absolute;left:40px;top:30px;width:460px;height:250px;border-radius:40px;background:radial-gradient(ellipse at center,rgba(255,255,255,.07),rgba(255,255,255,0) 70%)}
  .back-brand{position:absolute;left:0;right:0;top:0;bottom:0;display:flex;align-items:center;justify-content:center;gap:18px}
  .back-brand .brand-square{width:86px;height:86px;border:4px solid var(--on-red);border-radius:12px}
  .back-brand .brand-name{color:var(--on-red);font-size:34px;letter-spacing:2px}
</style>
</head>
<body>
<main class="stage">

  <section class="card card-front" aria-label="Business card front">
    <div class="brand">
      <span class="brand-square"></span>
      <span class="brand-name">Bramford<br>Holloway</span>
    </div>
    <div class="divider"></div>
    <div class="person">
      <p class="person-name">OWEN THACKERAY</p>
      <p class="person-title">Director</p>
      <ul class="contacts">
        <li><svg viewBox="0 0 12 12"><path fill="#a50e12" d="M2.5 1l2 2-1 1.3a6 6 0 0 0 4.2 4.2L9 7.5l2 2-1.3 1.5C5.5 11 1 6.5 1 2.3z"/></svg>+1 (888) 555-0142</li>
        <li><svg viewBox="0 0 12 12"><rect x="1" y="2.5" width="10" height="7" fill="#a50e12"/><path d="M1 3l5 3.6L11 3" stroke="#fff" fill="none"/></svg>info@bramfordhollowayinc.com</li>
        <li><svg viewBox="0 0 12 12"><circle cx="6" cy="6" r="5" fill="#a50e12"/><path d="M1 6h10M6 1c-2 2.5-2 7.5 0 10M6 1c2 2.5 2 7.5 0 10" stroke="#fff" stroke-width=".8" fill="none"/></svg>www.bramfordhollowayinc.com</li>
      </ul>
    </div>
    <div class="address-band">
      <svg viewBox="0 0 10 13"><path fill="#fff" d="M5 0a4.5 4.5 0 0 0-4.5 4.5C.5 8 5 13 5 13s4.5-5 4.5-8.5A4.5 4.5 0 0 0 5 0zm0 6.3a1.8 1.8 0 1 1 0-3.6 1.8 1.8 0 0 1 0 3.6z"/></svg>
      48 Elmsway Crt, Unit 210, Thornbury, ON K2P 0X4
    </div>
    <div class="base-line"></div>
  </section>

  <section class="card card-back" aria-label="Business card back">
    <div class="world-map" role="img" aria-label="Faint dotted world map watermark"></div>
    <div class="back-brand">
      <span class="brand-square"></span>
      <span class="brand-name">BRAMFORD<br>HOLLOWAY</span>
    </div>
  </section>

</main>
</body>
</html>
```